Design a New Business Card for Our Company

We are looking for fresh, unique, and a modern business card that reflects our roots as digital marketing agency focused on SEM.

Industry/Entity Type

Marketing

Contact Information for Business Card

looking for very unique out of the box designs. clean and modern that compliments our logo

Requirements
Must have
• colors should match our logo
• Front should have name, address, email, and phone/fax of the person, phone/fax are the same number
• back should have our url

```html
<!DOCTYPE html>
<html lang="en">
<head>
<meta charset="utf-8">
<title>Brightrow Media — Business Card</title>
<link href="https://fonts.googleapis.com/css2?family=Arimo:ital,wght@0,400;0,700;1,400&display=swap" rel="stylesheet">
<style>
  :root {
    --brand-blue: #1a63a5;
    --paper: #ffffff;
    --backdrop: #efefef;
    --ink: #222222;
    --ink-soft: #555555;
    --rule: #c9c9c9;
  }
  * { box-sizing: border-box; margin: 0; padding: 0; }
  html, body { width: 904px; height: 1200px; overflow: hidden; }
  body {
    background: var(--backdrop);
    font-family: "Arimo", Arial, sans-serif;
    color: var(--ink);
    position: relative;
  }
  .side-label {
    position: absolute;
    font-size: 30px;
    font-weight: 400;
    color: var(--ink);
  }
  .side-label--front { top: 30px; right: 60px; }
  .side-label--back { top: 630px; left: 32px; }

  .card {
    position: absolute;
    left: 172px;
    width: 560px;
    height: 340px;
    background: var(--paper);
    box-shadow: 0 4px 14px rgba(0,0,0,0.12);
    overflow: hidden;
  }
  .card--front { top: 120px; }
  .card--back { top: 700px; }
  .card__art { position: absolute; inset: 0; }

  .wordmark {
    position: absolute;
    display: flex;
    align-items: center;
    gap: 10px;
    font-family: "Arimo", Arial, sans-serif;
    font-weight: 700;
    font-size: 34px;
    letter-spacing: -0.5px;
    color: var(--brand-blue);
    white-space: nowrap;
  }
  .wordmark__dot {
    width: 26px; height: 26px;
    border-radius: 50%;
    background: var(--brand-blue);
    flex: none;
  }
  .card--front .wordmark { left: 124px; width: 312px; top: 80px; justify-content: center; }
  .card--back .wordmark { left: 0; width: 560px; top: 208px; justify-content: center; }

  .holder { position: absolute; left: 19px; top: 253px; }
  .holder__name { font-size: 14px; font-weight: 700; color: var(--brand-blue); }
  .holder__role { font-size: 11px; font-style: italic; margin-top: 4px; }

  .contact {
    position: absolute;
    left: 360px; top: 212px;
    width: 200px;
    font-size: 10px;
    color: var(--ink-soft);
  }
  .contact__address { line-height: 14px; padding-left: 14px; height: 38px; }
  .contact__list { list-style: none; padding-left: 14px; margin-top: 6px; }
  .contact__item { display: flex; align-items: center; gap: 9px; height: 23px; }
  .contact__icon {
    width: 18px; height: 15px;
    background: var(--brand-blue);
    color: var(--paper);
    font-size: 9px; font-weight: 700;
    display: flex; align-items: center; justify-content: center;
  }

  .site-url {
    position: absolute;
    left: 0; width: 560px; top: 260px;
    text-align: center;
    font-size: 11px;
    color: var(--paper);
  }
</style>
</head>
<body>
  <div class="side-label side-label--front">Front</div>
  <div class="side-label side-label--back">Back</div>

  <section class="card card--front" aria-label="Business card front">
    <svg class="card__art" width="560" height="340" viewBox="0 0 560 340" aria-hidden="true">
      <rect x="0" y="0" width="560" height="182" fill="var(--brand-blue)"/>
      <rect x="0" y="80" width="560" height="52" fill="var(--paper)"/>
      <polygon points="96,80 124,72 124,80" fill="var(--brand-blue)"/>
      <polygon points="96,132 124,140 124,132" fill="var(--brand-blue)"/>
      <polygon points="464,80 436,72 436,80" fill="var(--brand-blue)"/>
      <polygon points="464,132 436,140 436,132" fill="var(--brand-blue)"/>
      <rect x="124" y="56" width="312" height="100" rx="14" fill="var(--paper)"/>
      <line x1="360" y1="212" x2="360" y2="340" stroke="var(--rule)" stroke-width="1"/>
      <line x1="360" y1="251" x2="560" y2="251" stroke="var(--rule)" stroke-width="1"/>
    </svg>
    <div class="wordmark" style="top:88px"><span class="wordmark__dot"></span>Brightrow Media</div>

    <div class="holder">
      <p class="holder__name">Your Good Name</p>
      <p class="holder__role">Designation</p>
    </div>

    <div class="contact">
      <p class="contact__address">4870 Maple Crest Rd Glenfield,<br>CA 90210 USA</p>
      <ul class="contact__list">
        <li class="contact__item"><span class="contact__icon">t</span>555-204-7731</li>
        <li class="contact__item"><span class="contact__icon">f</span>555-204-7731</li>
        <li class="contact__item"><span class="contact__icon">e</span>hello@brightrowmedia.com</li>
      </ul>
    </div>
  </section>

  <section class="card card--back" aria-label="Business card back">
    <svg class="card__art" width="560" height="340" viewBox="0 0 560 340" aria-hidden="true">
      <rect x="0" y="261" width="560" height="79" fill="var(--brand-blue)"/>
      <polygon points="96,248 464,248 452,261 108,261" fill="var(--brand-blue)"/>
    </svg>
    <div class="wordmark"><span class="wordmark__dot"></span>Brightrow Media</div>
    <p class="site-url" style="top:253px">www.brightrowmedia.com</p>
  </section>
</body>
</html>
```